Talcott Land Surveyors Business Card

We are a land surveying company looking for a business card with a clean, sharp design. We would like for our design to portray our logo on one side, and contact information on the other w/ or w/o logo. Our colors preferred are navy blue, grey/silver, white and black. thank you!

Industry/Entity Type

Surveyor

Contact Information for Business Card

Talcott Land Surveyors
Gordon Pavlikova, P.L.S.
(781) 555-0193
Talcottlandsurveyors@mailbox.example
Talcottlandsurveyors.example
287 Willowmere Lane, Reading MA 01999

Requirements
Must have
• 1. Company Name
2. Personal name and title
3. phone number
4. email.
5. website
6. address

```html
<!DOCTYPE html>
<html lang="en">
<head>
<meta charset="utf-8">
<title>Talcott Land Surveyors – Business Card</title>
<link rel="stylesheet" href="https://fonts.googleapis.com/css2?family=Poppins:wght@300;400;700&display=swap">
<style>
  :root {
    --page: #e9e7e4;
    --card-top: #f4f6fb;
    --card-bottom: #dfe3ec;
    --navy: #17146a;
    --navy-deep: #0f0d52;
    --silver: #c7c8d3;
    --silver-dark: #5b5b66;
    --rose: #c79aa6;
    --ink: #12104d;
  }
  html, body {
    margin: 0;
    width: 1200px;
    height: 970px;
    overflow: hidden;
    background: var(--page);
    font-family: "Poppins", sans-serif;
  }
  .card-frame {
    position: absolute;
    left: 60px;
    top: 176px;
    width: 1080px;
    height: 618px;
  }
  .card {
    position: absolute;
    left: 0;
    top: 0;
    width: 1180px;
    height: 675px;
    transform: scale(0.9153);
    transform-origin: 0 0;
    border-radius: 34px;
    overflow: hidden;
    background: linear-gradient(160deg, var(--card-top), var(--card-bottom));
    box-shadow: 0 18px 40px rgba(0,0,0,0.18);
  }
  .card-waves {
    position: absolute;
    inset: 0;
    width: 100%;
    height: 100%;
  }
  .brand {
    position: absolute;
    left: 60px;
    top: 180px;
    width: 480px;
    text-align: center;
    color: var(--navy);
    font-weight: 700;
    font-size: 44px;
    letter-spacing: 6px;
    line-height: 1.2;
    text-transform: uppercase;
  }
  .brand-mark {
    display: block;
    width: 90px;
    height: 90px;
    margin: 0 auto 22px;
    border-radius: 50%;
    background: var(--navy);
  }
  .holder {
    position: absolute;
    right: 45px;
    top: 90px;
    margin: 0;
    font-size: 34px;
    font-weight: 700;
    color: var(--ink);
    letter-spacing: -0.5px;
  }
  .address {
    position: absolute;
    right: 45px;
    top: 398px;
    margin: 0;
    text-align: right;
    font-size: 26px;
    font-weight: 400;
    line-height: 35px;
    font-style: normal;
    color: var(--silver);
  }
  .contact-list {
    position: absolute;
    right: 45px;
    top: 510px;
    margin: 0;
    padding: 0;
    list-style: none;
    text-align: right;
    font-size: 26px;
    font-weight: 400;
    line-height: 38px;
  }
  .contact-item {
    display: flex;
    justify-content: flex-end;
    align-items: center;
    gap: 14px;
    color: var(--silver);
  }
  .contact-item.email { color: var(--rose); }
  .contact-icon {
    width: 28px;
    height: 28px;
    flex: none;
  }
</style>
</head>
<body>
  <div class="card-frame">
    <section class="card" aria-label="Business card">
      <svg class="card-waves" viewBox="0 0 1180 675" preserveAspectRatio="none" aria-hidden="true">
        <defs>
          <linearGradient id="navyBody" x1="0" y1="0" x2="1" y2="1">
            <stop offset="0" stop-color="#1f1c7a"/>
            <stop offset="1" stop-color="#0f0d52"/>
          </linearGradient>
          <linearGradient id="silverSwoosh" x1="0" y1="0" x2="1" y2="0">
            <stop offset="0" stop-color="#4a4a55"/>
            <stop offset="0.6" stop-color="#9d9ca8"/>
            <stop offset="1" stop-color="#5b5b66"/>
          </linearGradient>
          <linearGradient id="roseSwoosh" x1="0" y1="0" x2="1" y2="0">
            <stop offset="0" stop-color="#8f7d92"/>
            <stop offset="0.45" stop-color="#d3a9b4"/>
            <stop offset="1" stop-color="#3d3a7a"/>
          </linearGradient>
        </defs>
        <!-- silver swoosh -->
        <path d="M0 485 C120 540 260 560 380 520 C450 495 510 450 560 398 C500 470 420 530 330 555 C210 585 90 560 0 520 Z" fill="url(#silverSwoosh)"/>
        <!-- navy band at lower left -->
        <path d="M0 555 C90 600 210 615 330 590 C230 640 120 660 60 675 L0 675 Z" fill="url(#navyBody)"/>
        <!-- rose swoosh -->
        <path d="M0 530 C130 590 300 600 430 545 C600 470 780 330 960 300 C1030 288 1080 290 1110 292 C1020 296 900 320 790 380 C640 460 520 560 380 600 C240 640 100 610 0 570 Z" fill="url(#roseSwoosh)"/>
        <!-- main navy body -->
        <path d="M100 628 C250 640 380 610 480 560 C620 490 740 370 880 335 C980 312 1080 315 1180 338 L1180 675 L110 675 C90 660 90 640 100 628 Z" fill="url(#navyBody)"/>
      </svg>

      <div class="brand">
        <span class="brand-mark" aria-hidden="true"></span>
        Talcott<br>Land Surveyors
      </div>

      <h1 class="holder">Gordon Pavlikova, P.L.S.</h1>

      <address class="address">287 Willowmere Lane<br>Reading MA 01999</address>

      <ul class="contact-list">
        <li class="contact-item phone">(781) 555-0193
          <svg class="contact-icon" viewBox="0 0 28 28" aria-hidden="true">
            <circle cx="14" cy="14" r="13" fill="#e9eaf2"/>
            <rect x="9.5" y="7" width="9" height="14" rx="2" fill="none" stroke="#17146a" stroke-width="2"/>
          </svg>
        </li>
        <li class="contact-item email">Talcottlandsurveyors@mailbox.example
          <svg class="contact-icon" viewBox="0 0 28 28" aria-hidden="true">
            <circle cx="14" cy="14" r="13" fill="#e9eaf2"/>
            <rect x="7.5" y="9" width="13" height="10" rx="1" fill="none" stroke="#17146a" stroke-width="1.8"/>
            <path d="M7.5 9.5 L14 15 L20.5 9.5" fill="none" stroke="#17146a" stroke-width="1.8"/>
          </svg>
        </li>
        <li class="contact-item web">Talcottlandsurveyors.example
          <svg class="contact-icon" viewBox="0 0 28 28" aria-hidden="true">
            <circle cx="14" cy="14" r="13" fill="#e9eaf2"/>
            <circle cx="14" cy="14" r="7" fill="none" stroke="#17146a" stroke-width="1.6"/>
            <ellipse cx="14" cy="14" rx="3" ry="7" fill="none" stroke="#17146a" stroke-width="1.4"/>
            <path d="M7 14 H21" stroke="#17146a" stroke-width="1.4"/>
          </svg>
        </li>
      </ul>
    </section>
  </div>
</body>
</html>
```